Web Page Design for a Website that Provides Tutoring

I am looking to create an online tutoring website. The website will allow parents or students to contact tutors with a view to instructing them to tutor themselves or their children.

The name of the website is LendYourLessons.

This brief is to create the design for one of the web pages for this web site. I am hoping the same designer will be available to design other pages.

The page I want designed is one of the more complex and I have attached the design as an excel spreadsheet. The web page needs to include all the items on this page but if you want to change the positioning of the items then Im fine with that.

I recently had two logos created for this website. My favourite is the one with a mortar board but im not sure I like the colours. I have attached both of these logos and you can use either of them, change the colours or create something different. I just want a design pleasing to the eye. If the logo is changed I would like that in a seperate file.

So can you please submit designs for this page. I have attached the two logos which you can use, change or if you feel you have a better idea then you can use that.

On the spreadsheet the Send Message, Favourite etc are buttons.

Target Market(s)

People who want to better themselves.
Possible middle class to upper class.

Industry/Entity Type

Tutoring

Number of Pages Required

1 page

Requirements
Must have
• The designs must have alot of the information attached in the spreadsheet.

```html
<!DOCTYPE html>
<html lang="en">
<head>
<meta charset="utf-8">
<title>LendYourLessons – Tutor Profile</title>
<link href="https://fonts.googleapis.com/css2?family=Roboto:ital,wght@0,300;0,400;0,500;0,700;1,300&display=swap" rel="stylesheet">
<style>
:root{
  --bar:#39393b;
  --page:#efefef;
  --panel:#ffffff;
  --orange:#f7941d;
  --green:#0f9d58;
  --teal:#4db591;
  --red:#c94a4a;
  --taken:#d81f1f;
  --purple:#b156f0;
  --ink:#333333;
  --muted:#666666;
  --faint:#c4c4c4;
  --box:#ececec;
  --field:#f1f1f1;
}
*{margin:0;padding:0;box-sizing:border-box}
html,body{width:1200px;height:2871px;overflow:hidden}
body{position:relative;background:var(--page);font-family:'Roboto',sans-serif;color:var(--ink)}
.abs{position:absolute}

/* header */
.topbar{position:absolute;left:0;top:0;width:1200px;height:77px;background:var(--bar)}
.brand{position:absolute;left:86px;top:14px;font-size:40px;font-weight:700;color:var(--orange);letter-spacing:-1px;display:flex;align-items:center;gap:10px}
.brand-mark{width:22px;height:22px;background:var(--orange)}
.search{position:absolute;left:471px;top:21px;width:365px;height:36px;background:#fff;border-radius:3px}
.search span{position:absolute;left:26px;top:9px;font-size:14px;font-style:italic;color:#b8b8b8;font-weight:300}
.search svg{position:absolute;right:10px;top:7px}
.account{position:absolute;top:29px;font-size:16px;color:#fff}
.mainnav{position:absolute;left:0;top:77px;width:1200px;height:38px;background:#fff;border-bottom:1px solid #ddd}
.navlink{position:absolute;top:10px;font-size:15px;color:var(--ink);transform:translateX(-50%)}

/* panel */
.panel{position:absolute;left:86px;top:172px;width:1028px;height:2542px;background:var(--panel)}
.section-title{position:absolute;left:126px;font-size:20px;color:var(--faint);font-weight:400}

.tutor-name{left:170px;top:245px;font-size:32px;font-weight:400}
.online-dot{left:330px;top:262px;width:8px;height:8px;border-radius:50%;background:#2ecc71}
.tutor-role{left:170px;top:288px;font-size:14px;color:var(--muted)}
.photo{left:170px;top:312px;width:236px;height:235px;background:linear-gradient(160deg,#4a5a48,#8a7262 55%,#3c3a36)}
.btn{position:absolute;display:flex;align-items:center;justify-content:center;color:#fff;font-size:15px}
.btn-message{left:170px;top:559px;width:163px;height:50px;background:var(--teal)}
.btn-fav{left:339px;top:559px;width:67px;height:50px;background:var(--red)}
.intro{left:471px;top:312px;width:559px;height:235px;background:var(--box);padding:26px 28px;font-size:15px;line-height:27px;color:#555}
.intro h3{font-size:15px;font-weight:500;color:var(--ink);margin-bottom:8px}
.intro p+p{margin-top:24px}
.intro-notch{left:459px;top:376px;width:0;height:0;border-top:12px solid transparent;border-bottom:12px solid transparent;border-right:12px solid var(--box)}
.btn-review{left:905px;top:559px;width:125px;height:38px;background:var(--orange);font-size:11px;border-radius:2px}

/* info */
.info{font-size:15px}
.info .lbl{position:absolute;color:var(--ink)}
.info .val{position:absolute;color:var(--muted)}
.info .ok{color:var(--green)}

/* subjects table */
.subjects{position:absolute;left:149px;top:1112px;border-collapse:collapse;font-size:15px;width:898px}
.subjects th{font-weight:400;height:31px;vertical-align:middle;text-align:center;color:var(--ink)}
.subjects th.dim{color:var(--faint)}
.subjects td{height:40px;border:2px solid var(--orange);text-align:center;color:var(--ink)}
.subjects td.subject{background:var(--orange);color:#fff;text-align:left;padding-left:24px;font-weight:500}

/* availability */
.tabs{position:absolute;left:199px;top:1411px;width:800px;height:38px}
.tab{position:absolute;top:0;height:38px;line-height:38px;font-size:15px;color:var(--faint);transform:translateX(-50%)}
.tab.active{left:60px;width:121px;text-align:center;background:var(--bar);color:#fff;font-weight:500}
.schedule{left:199px;top:1449px;width:789px;height:211px;background:#fff;box-shadow:0 1px 4px rgba(0,0,0,.25)}
.slot-time{position:absolute;left:300px;font-size:15px;color:var(--ink);transform:translateY(-50%)}
.slot-bar{position:absolute;left:358px;width:628px;height:11px;transform:translateY(-50%)}
.legend{position:absolute;right:216px;top:1668px;font-size:15px;display:flex;gap:26px}

/* reviews */
.summary{position:absolute;left:86px;width:1028px;top:1838px;text-align:center;font-size:21px}
.summary em{font-style:normal;color:var(--orange)}
.stars{color:var(--orange);letter-spacing:1px}
.star-empty{color:#aaa}
.star-half{background:linear-gradient(90deg,var(--orange) 50%,#ddd 50%);-webkit-background-clip:text;background-clip:text;color:transparent}
.divider{position:absolute;left:249px;width:779px;height:3px;background:linear-gradient(90deg,rgba(247,148,29,0),rgba(247,148,29,.55) 30%,rgba(247,148,29,.55) 70%,rgba(247,148,29,0))}
.reviewer{font-size:21px}
.avatar{width:65px;height:63px}
.rev-date{font-size:21px;color:var(--muted)}
.rev-stars{font-size:21px}
.rev-text{width:331px;height:136px;background:var(--box);padding:20px 24px;font-size:15px;line-height:20px;text-align:center;color:var(--ink)}

.form-title{position:absolute;left:86px;width:1028px;top:2324px;text-align:center;font-size:21px}
.field{position:absolute;background:var(--field);font-size:20px;font-style:italic;font-weight:300;color:#c2c2c2;padding:10px 24px}
.btn-submit{left:806px;top:2603px;width:126px;height:38px;background:var(--orange);font-size:11px;border-radius:2px}

/* footer */
.footnav .navlink{top:2752px}
.bottombar{position:absolute;left:0;top:2813px;width:1200px;height:58px;background:var(--bar)}
.copyright{position:absolute;left:86px;top:20px;font-size:15px;color:#bdbdbd}
.social{position:absolute;right:86px;top:19px;display:flex;gap:22px}
.social span{width:20px;height:20px;border-radius:50%;background:#9a9a9a}
</style>
</head>
<body>

<header class="topbar">
  <div class="brand"><span class="brand-mark"></span>LendYourLessons</div>
  <div class="search">
    <span>Find Tutors, Students etc</span>
    <svg width="22" height="22" viewBox="0 0 22 22" fill="none" stroke="#666" stroke-width="2.4"><circle cx="9" cy="9" r="6.5"/><path d="M14 14l6 6"/></svg>
  </div>
  <a class="account" style="left:947px">Sign in</a>
  <a class="account" style="left:1016px">Register</a>
</header>
<nav class="mainnav">
  <span class="navlink" style="left:299px">Home</span>
  <span class="navlink" style="left:440px">Search</span>
  <span class="navlink" style="left:593px">Students</span>
  <span class="navlink" style="left:746px">Tutors</span>
  <span class="navlink" style="left:894px">Contact</span>
</nav>

<main>
  <div class="panel"></div>

  <!-- overview -->
  <h2 class="section-title" style="top:186px">Overview</h2>
  <h1 class="abs tutor-name">Daniel Moreno</h1>
  <span class="abs online-dot" style="left:374px"></span>
  <p class="abs tutor-role">(Algebra-Chemistry Tutor )</p>
  <div class="abs photo" role="img" aria-label="Portrait photo of the tutor outdoors"></div>
  <a class="btn btn-message">SEND MESSAGE</a>
  <a class="btn btn-fav" aria-label="Add to favourites">
    <svg width="24" height="22" viewBox="0 0 24 22" fill="none" stroke="#fff" stroke-width="2"><path d="M12 20S2 13.5 2 7.2A5 5 0 0 1 12 5a5 5 0 0 1 10 2.2C22 13.5 12 20 12 20z"/></svg>
  </a>
  <span class="abs intro-notch"></span>
  <div class="abs intro">
    <h3>Some words from the tutor:</h3>
    <p>“Hi to everyone. My name is Daniel and im an Algebra and Chemistry Tutor. Lorem ipsum dolor sit amet, consectetur adipiscing elit.</p>
    <p>Sed rhoncus nunc non augue consectetur, a faucibus diam molestie. Suspendisse tortor enim, dictum in orci vitae, porttitor sollicitudin felis.”</p>
  </div>
  <a class="btn btn-review">WRITE REVIEW</a>

  <!-- information -->
  <h2 class="section-title" style="top:701px">Information</h2>
  <div class="info">
    <span class="lbl" style="left:260px;top:763px">Review Score:</span><span class="val" style="left:412px;top:763px">4.5/5</span>
    <span class="lbl" style="left:260px;top:790px">Reliability:</span><span class="val" style="left:412px;top:790px">4.0/5.0</span>
    <span class="lbl" style="left:260px;top:819px">Puncuality:</span><span class="val" style="left:412px;top:819px">4.6/5</span>
    <span class="lbl" style="left:593px;top:763px">Member Since:</span><span class="val" style="left:750px;top:763px">09/2016</span>
    <span class="lbl" style="left:593px;top:790px">Last Loggen in:</span><span class="val ok" style="left:750px;top:790px">Active Now!</span>
    <span class="lbl" style="left:260px;top:878px">Tutoring Type:</span><span class="val" style="left:412px;top:878px">In personal only</span>
    <span class="lbl" style="left:260px;top:907px">Willing to Travel:</span><span class="val" style="left:412px;top:907px">Home only</span>
    <span class="lbl" style="left:593px;top:878px">Age:</span><span class="val" style="left:750px;top:878px">20</span>
    <span class="lbl" style="left:593px;top:905px">DBS(CRB):</span><span class="val ok" style="left:750px;top:905px">Checked</span>
  </div>

  <!-- subjects -->
  <h2 class="section-title" style="top:1036px">Subjects Taught</h2>
  <table class="subjects">
    <colgroup><col style="width:148px"><col style="width:132px"><col style="width:139px"><col style="width:125px"><col style="width:140px"><col style="width:109px"><col style="width:105px"></colgroup>
    <tr><th></th><th>Primary</th><th>Secondary</th><th>GSE</th><th>Advanced</th><th class="dim">University</th><th class="dim">Adult Learner</th></tr>
    <tr><td class="subject">BIOLOGY</td><td>25$</td><td>30$</td><td>35$</td><td>35$</td><td>N/A</td><td>N/A</td></tr>
    <tr><td class="subject">CHEMISTRY</td><td>25$</td><td>30$</td><td>35$</td><td>35$</td><td>N/A</td><td>N/A</td></tr>
  </table>

  <!-- availability -->
  <h2 class="section-title" style="top:1327px">Availability</h2>
  <div class="tabs">
    <span class="tab active" style="transform:none;left:0">Monday</span>
    <span class="tab" style="left:174px">Tuesday</span>
    <span class="tab" style="left:299px">Wednesday</span>
    <span class="tab" style="left:427px">Thursday</span>
    <span class="tab" style="left:536px">Friday</span>
    <span class="tab" style="left:645px">Saturday</span>
    <span class="tab" style="left:754px">Sunday</span>
  </div>
  <div class="abs schedule"></div>
  <span class="slot-time" style="top:1476px">7-8</span><span class="slot-bar" style="top:1476px;background:var(--green)"></span>
  <span class="slot-time" style="top:1512px">8-9</span><span class="slot-bar" style="top:1512px;background:var(--orange)"></span>
  <span class="slot-time" style="top:1550px">4-5</span><span class="slot-bar" style="top:1550px;background:var(--green)"></span>
  <span class="slot-time" style="top:1589px">5-6</span><span class="slot-bar" style="top:1589px;background:var(--purple)"></span>
  <span class="slot-time" style="top:1625px">7-8</span><span class="slot-bar" style="top:1625px;background:var(--taken)"></span>
  <div class="legend">
    <span style="color:var(--green)">• Available</span>
    <span style="color:var(--orange)">• Reserved</span>
    <span style="color:var(--taken)">• Taken</span>
    <span style="color:var(--purple)">• Not Available</span>
  </div>

  <!-- reviews -->
  <h2 class="section-title" style="top:1765px">Reviews</h2>
  <p class="summary">Daniel Moreno has <em>2</em> reviews with an average review score of:&nbsp; 4.5 <span class="stars" style="font-size:17px">★★★★<span class="star-half">★</span></span></p>
  <div class="divider" style="top:1894px"></div>

  <article>
    <span class="abs reviewer" style="left:226px;top:1955px">Owen Hartley</span>
    <div class="abs avatar" style="left:226px;top:1989px;background:linear-gradient(150deg,#c98f7a,#7b4a3f)" role="img" aria-label="Reviewer profile photo"></div>
    <span class="abs rev-date" style="left:454px;top:1970px">21/11/2016</span>
    <span class="abs stars rev-stars" style="left:456px;top:1998px">★★★★<span class="star-empty">☆</span></span>
    <p class="abs rev-text" style="left:643px;top:1949px">“Lorem ipsum dolor sit amet, consectetur adipisicing elit, sed do eiusmod tempor incididunt ut labore et dolore magna aliqua. Ut enim ad minim veniam, quis nostrud exercitation ullamco laboris nisi.”</p>
  </article>
  <div class="divider" style="top:2101px"></div>

  <article>
    <span class="abs reviewer" style="left:226px;top:2127px">Lucas Whitby</span>
    <div class="abs avatar" style="left:226px;top:2161px;background:linear-gradient(150deg,#b9a596,#5e5248)" role="img" aria-label="Reviewer profile photo"></div>
    <span class="abs rev-date" style="left:454px;top:2142px">21/11/2016</span>
    <span class="abs stars rev-stars" style="left:456px;top:2170px">★★★★<span class="star-half">★</span></span>
    <p class="abs rev-text" style="left:643px;top:2121px">“Lorem ipsum dolor sit amet, consectetur adipisicing elit, sed do eiusmod tempor incididunt ut labore et dolore magna aliqua. Ut enim ad minim veniam, quis nostrud exercitation ullamco laboris nisi.”</p>
  </article>
  <div class="divider" style="top:2294px"></div>

  <h3 class="form-title">Submit a review for Daniel Moreno</h3>
  <div class="field" style="left:264px;top:2370px;width:213px;height:51px">Tutee Name...</div>
  <div class="field" style="left:492px;top:2370px;width:212px;height:51px">Date/Time...</div>
  <div class="field" style="left:720px;top:2370px;width:212px;height:51px">Star rating...</div>
  <div class="field" style="left:264px;top:2438px;width:668px;height:150px;padding-top:14px">Some words for the Tutor...</div>
  <a class="btn btn-submit">SUBMIT REVIEW</a>
</main>

<footer>
  <nav class="footnav">
    <span class="navlink" style="left:299px">Home</span>
    <span class="navlink" style="left:440px">Search</span>
    <span class="navlink" style="left:593px">Students</span>
    <span class="navlink" style="left:746px">Tutors</span>
    <span class="navlink" style="left:894px">Contact</span>
  </nav>
  <div class="bottombar">
    <p class="copyright">Copyright 2016 LendYourLessons.example. All rights reserved.</p>
    <div class="social"><span></span><span></span><span></span><span></span></div>
  </div>
</footer>

</body>
</html>
```